Gardener needs an exciting new flyer design.

I'm a passionate gardener that requires a custom flyer design for a owner operator gardening business. Design will be for a DL flyer. I'm based on the Sunshine coast in Queensland Australia. My target audience is the residential market on the Sunshine coast. Business name is Tollmere Yards. My services are, lawn mowing, weeding, Eco Friendly fertilizing, green waste removal, Mulching, tree and shrub pruning, Full garden makeovers, hedging, pressure cleaning, privacy screening, Timber deck rejuvenation, Planting, Turf preparation and installation, and much more. Free no obligation quotes, reliable and friendly service, great rates. 12 years experience. Web www.tollmereyards.com.au - Phone 0418527036 - Email kip@tollmereyards.com.au I would like the design to portray a friendly and professional approach.

Target Market(s)

Residential

Industry/Entity Type

Gardener

Font styles to use
Serif

Colors
9ccb3b
abd037
3176b5

Requirements
Must have
• my services, my logo, my contact details,

```html
<!DOCTYPE html>
<html lang="en">
<head>
<meta charset="utf-8">
<title>Tollmere Yards – DL Flyer</title>
<link rel="stylesheet" href="https://fonts.googleapis.com/css2?family=Berkshire+Swash&family=Oswald:wght@500&family=Open+Sans:wght@400;600&family=Lobster&display=swap">
<style>
  :root {
    --page-bg: #e8e8e5;
    --leaf-dark: #1e6a2c;
    --leaf-mid: #3f8f2a;
    --lime: #9ccb3b;
    --lime-soft: #abd037;
    --brand-text: #2a7434;
    --ink: #1d1d1d;
    --white: #ffffff;
  }
  * { box-sizing: border-box; margin: 0; padding: 0; }
  html, body { width: 1200px; height: 1177px; overflow: hidden; }
  body { background: var(--page-bg); position: relative; font-family: "Open Sans", sans-serif; }

  .flyer {
    position: absolute; top: 128px; width: 450px; height: 948px;
    background: var(--white); overflow: hidden;
    box-shadow: 0 2px 8px rgba(0,0,0,.15);
  }
  .flyer--front { left: 90px; }
  .flyer--back { left: 604px; }

  .photo { position: absolute; left: 0; top: 0; width: 450px; }
  .flyer--front .photo { height: 420px;
    background: linear-gradient(160deg, #6f8c5c 0%, #9aa7b9 30%, #5f9a3d 55%, #8f86c9 80%, #3e7a2c 100%); }
  .flyer--back .photo { height: 470px;
    background: linear-gradient(150deg, #8d7bc6 0%, #b9d38c 35%, #9c86d0 60%, #5f9c3c 100%); }

  .shapes { position: absolute; left: 0; top: 0; }

  .badge {
    position: absolute; left: 300px; top: 272px; width: 138px; height: 138px;
    border-radius: 50%; background: var(--leaf-dark); border: 4px solid var(--white);
    display: flex; align-items: center; justify-content: center; flex-direction: column;
    color: var(--white); font-family: "Oswald", sans-serif;
  }
  .badge__ring { font-size: 13px; letter-spacing: 2px; }
  .badge__years { font-size: 24px; background: var(--leaf-dark); border-top: 2px solid var(--white); border-bottom: 2px solid var(--white); padding: 0 8px; margin: 3px 0; }

  .inset {
    position: absolute; border-radius: 50%; border: 5px solid var(--white);
    box-shadow: 0 2px 6px rgba(0,0,0,.25);
  }
  .inset--stones { left: 150px; top: 328px; width: 124px; height: 124px;
    background: radial-gradient(circle at 40% 40%, #b39a78, #6d8e3f); }
  .inset--hammock { left: 288px; top: 286px; width: 152px; height: 152px;
    background: radial-gradient(circle at 50% 45%, #c8d48a, #4f8a30); }

  .brand-name {
    position: absolute; left: 0; width: 100%; text-align: center;
    font-family: "Berkshire Swash", serif; color: var(--brand-text); font-weight: 400; line-height: 1;
  }
  .flyer--front .brand-name { top: 444px; font-size: 50px; }
  .flyer--back .brand-name { top: 472px; font-size: 52px; }

  .headline {
    position: absolute; left: 0; width: 100%; text-align: center; line-height: 1;
    font-family: "Oswald", sans-serif; font-weight: 500; color: var(--white);
    text-shadow: 0 1px 2px rgba(0,0,0,.25);
  }
  .flyer--front .headline { top: 512px; font-size: 21px; }
  .flyer--back .headline { top: 543px; font-size: 21px; }

  .services { position: absolute; left: 14px; top: 560px; width: 430px;
    display: grid; grid-template-columns: 198px 232px; row-gap: 9px; list-style: none; }
  .service { display: flex; align-items: center; gap: 8px; height: 24px;
    color: var(--white); font-size: 13.5px; font-weight: 600; text-shadow: 0 1px 1px rgba(0,0,0,.2); }
  .service__icon { width: 24px; height: 24px; border-radius: 5px; background: var(--leaf-dark);
    border: 1.5px solid var(--white); flex: none; position: relative; }
  .service__icon::after { content: ""; position: absolute; left: 6px; top: 6px; width: 9px; height: 9px;
    border-radius: 50%; background: var(--lime); }

  .about { position: absolute; left: 26px; width: 398px; top: 592px; text-align: center;
    color: var(--white); font-size: 13px; font-weight: 600; line-height: 1.45; text-shadow: 0 1px 1px rgba(0,0,0,.2); }
  .about p + p { margin-top: 18px; }
  .about__sign { position: absolute; left: 0; width: 100%; top: 754px; text-align: center;
    font-family: "Lobster", serif; color: var(--white); font-size: 14px; }

  .footer { position: absolute; left: 0; top: 846px; width: 100%; text-align: center; }
  .footer__promise { font-size: 13.5px; color: var(--ink); line-height: 1.15; }
  .quote-pill {
    margin: 8px auto 0; width: 320px; height: 28px; border-radius: 14px;
    background: var(--leaf-mid); color: var(--white); display: flex; align-items: center; justify-content: center;
    gap: 8px; font-family: "Oswald", sans-serif; font-size: 17px; letter-spacing: .3px;
    box-shadow: 2px 3px 4px rgba(0,0,0,.25);
  }
  .quote-pill svg { width: 17px; height: 17px; }
  .footer__contact { margin-top: 10px; font-size: 13px; color: var(--ink); }
</style>
</head>
<body>

<section class="flyer flyer--front">
  <div class="photo" role="img" aria-label="Photo of a blue house with a lush front lawn, curved path and hydrangea flower beds"></div>
  <svg class="shapes" width="450" height="948" viewBox="0 0 450 948" aria-hidden="true">
    <defs>
      <linearGradient id="panelFront" x1="0" y1="0" x2="0" y2="1">
        <stop offset="0" stop-color="#c4e28f"/>
        <stop offset="0.55" stop-color="#86c04a"/>
        <stop offset="1" stop-color="#4b9527"/>
      </linearGradient>
    </defs>
    <path d="M0,330 C90,300 160,330 240,335 C320,340 390,320 450,280 L450,320 C380,370 300,380 220,375 C140,370 60,360 0,385 Z" fill="#1e6a2c"/>
    <path d="M0,385 C70,360 150,372 230,378 C320,384 390,365 450,320 L450,760 C360,830 220,810 120,800 C70,796 30,800 0,810 Z" fill="url(#panelFront)"/>
    <path d="M0,810 C60,792 140,800 230,810 C330,822 400,800 450,760 L450,790 C400,830 320,845 230,838 C140,830 60,820 0,830 Z" fill="#9ccb3b"/>
  </svg>
  <div class="badge">
    <span class="badge__ring">EXPERIENCE</span>
    <span class="badge__years">12 YEARS</span>
    <span class="badge__ring">EXPERIENCE</span>
  </div>
  <h1 class="brand-name">Tollmere Yards</h1>
  <h2 class="headline">YOUR GARDEN AND LAWN CARE SPECIALIST!</h2>
  <ul class="services">
    <li class="service"><span class="service__icon"></span>Lawn Mowing</li>
    <li class="service"><span class="service__icon"></span>Hedging</li>
    <li class="service"><span class="service__icon"></span>Weeding</li>
    <li class="service"><span class="service__icon"></span>Pressure Cleaning</li>
    <li class="service"><span class="service__icon"></span>Eco Friendly Fertilizing</li>
    <li class="service"><span class="service__icon"></span>Privacy Screening</li>
    <li class="service"><span class="service__icon"></span>Green Waste Removal</li>
    <li class="service"><span class="service__icon"></span>Timber Deck Rejuvenation</li>
    <li class="service"><span class="service__icon"></span>Mulching</li>
    <li class="service"><span class="service__icon"></span>Planting</li>
    <li class="service"><span class="service__icon"></span>Tree &amp; Shrub Pruning</li>
    <li class="service"><span class="service__icon"></span>Turf Preparation &amp; Installation</li>
    <li class="service"><span class="service__icon"></span>Full Garden Makeovers</li>
    <li class="service"><span class="service__icon"></span>And Much More</li>
  </ul>
  <div class="footer">
    <p class="footer__promise">Reliable and Friendly service<br>Great Rates</p>
    <div class="quote-pill">FREE QUOTES
      <svg viewBox="0 0 20 20" aria-hidden="true"><circle cx="10" cy="10" r="8.5" fill="none" stroke="#fff" stroke-width="1.6"/><path d="M7,5.5 L8.6,7.6 L7.8,8.8 C8.4,10.2 9.6,11.5 11.1,12.2 L12.3,11.4 L14.4,13 L13.3,14.6 C10,14.4 5.8,10.3 5.6,6.7 Z" fill="#fff"/></svg>
      0418527036</div>
    <p class="footer__contact">kip@tollmereyards.com.au &nbsp;|&nbsp; www.tollmereyards.com.au</p>
  </div>
</section>

<section class="flyer flyer--back">
  <div class="photo" role="img" aria-label="Photo of a stepping-stone garden path lined with purple lavender and salvia"></div>
  <svg class="shapes" width="450" height="948" viewBox="0 0 450 948" aria-hidden="true">
    <defs>
      <linearGradient id="panelBack" x1="0" y1="0" x2="0" y2="1">
        <stop offset="0" stop-color="#c4e28f"/>
        <stop offset="0.55" stop-color="#86c04a"/>
        <stop offset="1" stop-color="#4b9527"/>
      </linearGradient>
    </defs>
    <path d="M0,410 C50,372 110,362 170,372 L450,400 L450,420 L170,394 C110,388 50,405 0,440 Z" fill="#1e6a2c"/>
    <path d="M0,440 C50,405 110,390 170,396 L450,422 L450,760 C360,830 220,810 120,800 C70,796 30,800 0,810 Z" fill="url(#panelBack)"/>
    <path d="M0,810 C60,792 140,800 230,810 C330,822 400,800 450,760 L450,790 C400,830 320,845 230,838 C140,830 60,820 0,830 Z" fill="#9ccb3b"/>
  </svg>
  <div class="inset inset--stones" role="img" aria-label="Photo of a rock garden bed with mulch"></div>
  <div class="inset inset--hammock" role="img" aria-label="Photo of relaxing in a striped hammock on a lawn"></div>
  <h1 class="brand-name">Tollmere Yards</h1>
  <h2 class="headline">A BEAUTIFUL GARDEN DOESN'T HAPPEN BY ITSELF</h2>
  <div class="about">
    <p>Tollmere Yards is your garden and lawn care specialist, with a passion for gardening and a keen eye for detail you can rest assured you're in the right hands.</p>
    <p>My services are tailored to meet every individual clients needs. From a one time mow too regular lawn mowing, all aspects of garden care and even full garden makeovers.</p>
  </div>
  <p class="about__sign">Experience the best service on the east coast.</p>
  <div class="footer">
    <p class="footer__promise">Reliable and Friendly service<br>Great Rates</p>
    <div class="quote-pill">FREE QUOTES
      <svg viewBox="0 0 20 20" aria-hidden="true"><circle cx="10" cy="10" r="8.5" fill="none" stroke="#fff" stroke-width="1.6"/><path d="M7,5.5 L8.6,7.6 L7.8,8.8 C8.4,10.2 9.6,11.5 11.1,12.2 L12.3,11.4 L14.4,13 L13.3,14.6 C10,14.4 5.8,10.3 5.6,6.7 Z" fill="#fff"/></svg>
      0418527036</div>
    <p class="footer__contact">kip@tollmereyards.com.au &nbsp;|&nbsp; www.tollmereyards.com.au</p>
  </div>
</section>

</body>
</html>
```